Looking for a cool & simple business-card-design for digital agency

Hi!

We are a web agency that offers Reputation Management, Zorvik & Seo Services and software development. We like cool things, we like innovative styles.

We have uploaded our logo.

Project Deadline Extended Reason: Client does not want any designs with the colorful logo. Please send us submissions ONLY with the blac and white logo. What the client would like to see:1) Back of the card: is a silver logo on a black background2) front of the card with all the data, please use white background and black logo thank you Added Friday, May 8, 2015

Software

```html
<!DOCTYPE html>
<html lang="de">
<head>
<meta charset="utf-8">
<title>Nordweg AG – Visitenkarte</title>
<link rel="stylesheet" href="https://fonts.googleapis.com/css2?family=Source+Sans+3:ital,wght@0,400;0,600;0,700;1,700&display=swap">
<style>
  :root {
    --backdrop: #8a8a8a;
    --card-light: #ffffff;
    --card-dark: #231f20;
    --ink: #231f20;
    --ink-muted: #8f8f8f;
    --paper-text: #ffffff;
    --shadow: rgba(0, 0, 0, 0.35);
  }
  * { box-sizing: border-box; margin: 0; padding: 0; }
  html, body {
    width: 1200px;
    height: 907px;
    overflow: hidden;
    background: var(--backdrop);
    font-family: "Source Sans 3", Arial, sans-serif;
  }
  .card {
    position: absolute;
    left: 300px;
    width: 600px;
    height: 343px;
    box-shadow: 2px 4px 8px var(--shadow);
  }
  .card--front { top: 92px; background: var(--card-light); color: var(--ink); }
  .card--back  { top: 472px; background: var(--card-dark); color: var(--paper-text); }

  .brand {
    position: absolute;
    left: 0; right: 0;
    top: 70px;
    display: flex;
    flex-direction: column;
    align-items: center;
  }
  .brand__row { display: flex; align-items: center; gap: 12px; }
  .brand__square { width: 26px; height: 26px; background: var(--ink); }
  .brand__name { font-size: 34px; font-weight: 700; line-height: 1; letter-spacing: 0.5px; }
  .brand__tagline {
    margin-top: 6px;
    font-size: 15px;
    letter-spacing: 5px;
    font-weight: 400;
  }

  .rule {
    position: absolute;
    left: 39px; right: 40px;
    top: 212px;
    border-top: 1px solid var(--ink);
  }

  .contact {
    position: absolute;
    left: 39px;
    top: 228px;
    list-style: none;
    font-size: 14px;
  }
  .contact li { display: flex; align-items: center; height: 22.5px; }
  .contact svg { width: 14px; height: 14px; margin-right: 8px; fill: var(--ink); }

  .person {
    position: absolute;
    right: 36px;
    top: 225px;
    text-align: right;
  }
  .person__name { font-size: 20px; font-weight: 600; line-height: 1.2; }
  .person__title { font-size: 16px; color: var(--ink-muted); line-height: 1.3; margin-bottom: 4px; }
  .person__address { font-size: 14px; line-height: 1.4; font-style: normal; }

  .back-brand {
    position: absolute;
    left: 0; right: 0;
    top: 150px;
    display: flex;
    justify-content: center;
    align-items: center;
    gap: 14px;
  }
  .back-brand__square { width: 34px; height: 34px; background: var(--paper-text); }
  .back-brand__name { font-size: 44px; font-weight: 700; line-height: 1; }
  .back-url {
    position: absolute;
    left: 0; right: 0;
    top: 283px;
    text-align: center;
    font-size: 14px;
    font-weight: 700;
    font-style: italic;
    letter-spacing: 3.5px;
  }
</style>
</head>
<body>
  <section class="card card--front">
    <div class="brand">
      <div class="brand__row">
        <span class="brand__square"></span>
        <span class="brand__name">Nordweg AG</span>
      </div>
      <span class="brand__tagline">DIGITALE STRATEGIEN</span>
    </div>

    <div class="rule"></div>

    <ul class="contact">
      <li>
        <svg viewBox="0 0 16 16" aria-hidden="true"><path d="M4 1l3 3-2 2c1 2 3 4 5 5l2-2 3 3-2 2C7 14 2 9 2 3z"/></svg>
        127 345 9876
      </li>
      <li>
        <svg viewBox="0 0 16 16" aria-hidden="true"><rect x="4" y="1" width="8" height="4"/><rect x="1" y="6" width="14" height="6"/><rect x="4" y="10" width="8" height="5"/></svg>
        345 345 9876
      </li>
      <li>
        <svg viewBox="0 0 16 16" aria-hidden="true"><path d="M1 3h14v10H1z"/><path d="M1 3l7 6 7-6" fill="none" stroke="#fff" stroke-width="1.3"/></svg>
        info@yourname.com
      </li>
      <li>
        <svg viewBox="0 0 16 16" aria-hidden="true"><g fill="none" stroke="#231f20" stroke-width="1.1"><circle cx="8" cy="8" r="6.5"/><ellipse cx="8" cy="8" rx="3" ry="6.5"/><path d="M1.5 8h13M2.5 4.5h11M2.5 11.5h11"/></g></svg>
        www.yourweb.com
      </li>
    </ul>

    <div class="person">
      <p class="person__name">Your name</p>
      <p class="person__title">Job Title</p>
      <address class="person__address">Suite 102 Street name<br>State, Zip 2034,Country</address>
    </div>
  </section>

  <section class="card card--back">
    <div class="back-brand">
      <span class="back-brand__square"></span>
      <span class="back-brand__name">Nordweg AG</span>
    </div>
    <p class="back-url">www.yourweb.com</p>
  </section>
</body>
</html>
```